Rather Likely The Brightest Venture
Website for Life Coach
Rather Likely The Brightest Venture - Personal Care
Creative Brief
Personal Care
www.bluelanternhour.com
Website design for inspirational and motivational training company. Initial focus of the website is to promote trainer for life coach and inspirational speaker engagements with plan to expend into seminar and web based trainings in 2013.
General feel to be very upbeat, happy, feel good, simple and easy to navigate. !!When referring to the holding page of Blue Lantern Hour (which I think looks crap) please note the writing in the Logo of the name should be in Black!!
left side
http://www.quostelbury.com/
http://www.drwabble.com/
http://www.nora-pellham.com/
Home page to include areas for the following: Top banner showing logo, quote and small picture of face of company. Below this a thicker banner with sunflower field picture (in future to be a video link) and beside it text of an inspirational quote that will change on a regular basis. This to also include an opt in button where they can provide email address to be contacted or receive blogs and articles direct to their account. Links to other pages: home, the way, live it, who is he, contact me, archive Home page to also include a Short text intro to what blue lantern hour is all about with a picture of face of company again. Below this Space for most recent blog or article in full (to be changed on a regular basis) Opt in button at bottom of page Links at bottom of page to affiliated websites The opt in button to be at top and bottom of all pages with affiliate web links at bottom of all pages. Additional pages: The Way: A page describing the lifestyle being coached and it's different sections. There are 6 text sections in total on this page, each with a matching inspirational image to it. Live It: Introducing the concept of coaching. Images and text again with one testimonial at the top and a list of testimonials at the bottom Who Is He: A simply text and images page for bio information Contact: listing of ways in which to contact me. Also a space where they can fill out name, contact, and question or request. The submit button will automatically send this to an email. Archive: a simple listing of previous blogs and articles. These to be listed at top with a click on link to where they are further down the page

```html
<!DOCTYPE html>
<html lang="en">
<head>
<meta charset="utf-8">
<title>Blue Lantern Hour</title>
<link href="https://fonts.googleapis.com/css2?family=Arimo:ital,wght@0,400;0,700;1,400;1,700&family=Open+Sans:wght@400;600;700&display=swap" rel="stylesheet">
<style>
  :root{
    --green-dark:#0f4a1c;
    --green:#1d6b2a;
    --green-light:#3c8f3a;
    --orange:#f08a12;
    --orange-deep:#d9660a;
    --yellow:#f6c21c;
    --sky:#dfe9f3;
    --text:#333;
    --white:#fff;
  }
  *{box-sizing:border-box;margin:0;padding:0}
  html,body{width:1200px;height:1044px;overflow:hidden}
  body{font-family:"Arimo",Arial,sans-serif;color:var(--text);position:relative;
    background:linear-gradient(90deg,#e7f0f8 0%,var(--sky) 60%,#c9d9ea 100%)}
  .backdrop{position:absolute;left:0;top:0;width:560px;height:1044px;
    background:linear-gradient(90deg,#e9a62a 0%,#f3c65a 45%,rgba(223,233,243,0) 100%)}
  .header{position:absolute;left:0;top:0;width:1200px;height:140px;
    background:linear-gradient(180deg,#1f6b2b,var(--green-dark));}
  .brand{position:absolute;left:100px;top:26px;display:flex;align-items:center;gap:12px}
  .brand-dot{width:58px;height:58px;border-radius:50%;background:var(--yellow)}
  .brand-name{font-family:"Arimo",sans-serif;font-weight:700;font-size:34px;color:var(--white)}
  .utility{position:absolute;right:52px;top:6px;display:flex;gap:10px;align-items:center;font-size:12px;font-weight:700;color:var(--white)}
  .utility .circle{width:24px;height:24px;border-radius:50%;background:#e9eef2}
  .utility a{color:var(--white);text-decoration:none;margin-left:14px}
  .contact{position:absolute;right:52px;top:44px;text-align:right;color:var(--white)}
  .contact .phone{font-size:32px;font-weight:700;letter-spacing:.5px;line-height:38px}
  .contact .email{font-size:19px;font-weight:700;line-height:24px;margin-top:4px}
  .page{position:absolute;left:107px;top:168px;width:983px;height:870px;
    background:rgba(255,255,255,.55);border-radius:10px}
  .nav{position:absolute;left:0;top:6px;width:983px;height:32px;border-radius:8px 8px 0 0;
    background:linear-gradient(180deg,var(--green-light),var(--green-dark));display:flex}
  .nav a{flex:1;text-align:center;line-height:32px;color:var(--white);font-weight:700;font-size:14px;
    text-decoration:none;border-right:1px solid rgba(255,255,255,.35)}
  .nav a:last-child{border-right:0}
  .hero{position:absolute;left:0;top:40px;width:818px;height:284px;
    background:linear-gradient(180deg,#f4f4f4 0%,#d9d9d9 55%,#8a8a8a 100%)}
  .hero-quote{position:absolute;left:0;bottom:8px;width:818px;height:36px;background:rgba(20,20,20,.82);
    color:var(--white);font-style:italic;font-weight:700;font-size:15px;line-height:36px;padding-left:24px}
  .thumbs{position:absolute;left:828px;top:40px;width:148px;display:flex;flex-direction:column;gap:8px}
  .thumb{height:65px;border:3px solid var(--white);background:linear-gradient(135deg,#c9a68a,#6d5a4e 60%,#d8d2cc)}
  .welcome{position:absolute;left:8px;top:342px;width:645px;height:296px;background:var(--white);border:1px solid #c8c8c8;padding:14px 18px}
  .welcome h1{font-family:"Open Sans",sans-serif;font-size:17px;color:var(--green);font-weight:700;margin-bottom:12px}
  .welcome p{font-size:11.5px;line-height:15px;margin-bottom:11px}
  .join{position:absolute;left:668px;top:342px;width:308px;height:296px;border-radius:6px;
    background:linear-gradient(180deg,var(--orange) 0%,#f5a52e 60%,var(--orange-deep) 100%);color:var(--white);padding:16px 20px}
  .join h2{font-family:"Arimo",sans-serif;font-weight:400;font-size:34px;margin-bottom:18px}
  .join blockquote{font-family:"Arimo",sans-serif;font-size:19px;line-height:23px;text-align:center;margin-bottom:18px}
  .join .sign{text-align:right;font-size:14px;line-height:17px}
  .register{position:absolute;left:8px;top:648px;width:968px;height:120px;background:var(--white);text-align:center;padding-top:12px}
  .register p{font-size:14.5px;line-height:19px}
  .register .mail{color:var(--orange-deep)}
  .register strong{font-size:16px}
  .cta{display:inline-flex;align-items:center;gap:8px;margin-top:8px;height:30px;padding:0 22px 0 10px;border-radius:15px;
    background:linear-gradient(180deg,#ffa733,var(--orange-deep));color:var(--white);font-weight:700;font-size:17px;text-decoration:none}
  .footer{position:absolute;left:0;top:780px;width:983px;height:84px;border-radius:0 0 10px 10px;
    background:linear-gradient(180deg,#1f6b2b,var(--green-dark))}
  .footer .brand{left:14px;top:14px}
  .footer .brand-dot{width:50px;height:50px}
  .footer .brand-name{font-size:28px}
  .footer-links{position:absolute;right:18px;top:22px;font-size:12px;font-weight:700;color:var(--white);text-align:right}
  .footer-links a{color:var(--white);text-decoration:none}
  .copyright{margin-top:10px;font-size:9.5px;font-weight:400}
</style>
</head>
<body>
  <div class="backdrop" role="img" aria-label="Sunflower in full bloom filling the left background"></div>

  <header class="header">
    <div class="brand"><span class="brand-dot"></span><span class="brand-name">Blue Lantern Hour</span></div>
    <div class="utility">
      <span class="circle"></span><span class="circle"></span><span class="circle"></span>
      <a href="#">HOME</a><a href="#">CONTACT US</a><a href="#">SITEMAP</a>
    </div>
    <div class="contact">
      <div class="phone">CALL: 035-0987 6614</div>
      <div class="email">Email: info@bluelanternhour.com</div>
    </div>
  </header>

  <main class="page">
    <nav class="nav">
      <a href="#">HOME</a><a href="#">THE WAY</a><a href="#">LIVE IT</a><a href="#">WHO IS HE</a><a href="#">CONTACT US</a><a href="#">ARCHIVE</a>
    </nav>

    <section class="hero" role="img" aria-label="Group of smiling business people standing together">
      <div class="hero-quote">"Living each day as your favorite is a simple matter of choice. And the power of that choice lies within you."</div>
    </section>

    <div class="thumbs">
      <div class="thumb" role="img" aria-label="Team meeting photo"></div>
      <div class="thumb" role="img" aria-label="Colleagues talking photo"></div>
      <div class="thumb" role="img" aria-label="Coach presenting photo"></div>
      <div class="thumb" role="img" aria-label="Smiling man portrait"></div>
    </div>

    <section class="welcome">
      <h1>Welcome to 'Blue Lantern Hour' - The Fast Track Tools to a Better Life</h1>
      <p>Caught up in a busy, non stop world?<br>Tired of being at the mercy of up and down moods?<br>Fed up with nothing days that just drift by, out of your control?</p>
      <p><strong>Life is too short for it to be this way.</strong></p>
      <p>What if, just like one of your favorite days, you could 'choose' to live every day with passion, laughter and joy?</p>
      <p>Well, there is a way. We call it the 'Blue Lantern Hour' way. That's right, peace, happiness and personal empowerment can all be yours without spending the rest of your life standing on your head in meditation on a mountain top.</p>
      <p>It's quite simply a choice. And with our clear, concise and complete set of life changing tools that choice will be yours.</p>
    </section>

    <aside class="join">
      <h2>Join FREE today</h2>
      <blockquote>"Living each day as your favorite is a simple matter of choice. And the power of that choice lies within you."</blockquote>
      <div class="sign">Tom Halvard<br>Founder, Blue Lantern Hour</div>
    </aside>

    <section class="register">
      <p>Register now and start receiving our monthly motivational article and weekly blog or drop us an email:<span class="mail">info@bluelanternhour.com</span>.<br>
      The moment our website is fully live we will send you more information to ensure you<br>
      <strong>start living each day as your favorite... from TODAY.</strong></p>
      <a class="cta" href="#">
        <svg width="22" height="16" viewBox="0 0 22 16" aria-hidden="true"><path d="M2 5h10V1l9 7-9 7v-4H2z" fill="#fff"/></svg>
        CLICK HERE TO JOIN
      </a>
    </section>

    <footer class="footer">
      <div class="brand"><span class="brand-dot"></span><span class="brand-name">Blue Lantern Hour</span></div>
      <div class="footer-links">
        <a href="#">Home</a> | <a href="#">The Way</a> | <a href="#">Live It</a> | <a href="#">Who is He</a> | <a href="#">Contact Us</a> | <a href="#">Archive</a>
        <div class="copyright">Copyright © 2013 www.bluelanternhour.com &nbsp;&nbsp; PRIVACY POLICY - SITE MAP</div>
      </div>
    </footer>
  </main>
</body>
</html>
```